Time for a better IT consulting company?

We are a mobile computer consulting company, taking care of client's issues remotely or at their site. Website of company www.qr-lumotek.com. Business card is an example of marketing so far.
We moved this year but we still service our existing clients. We have expanded our number of technicians available. We would like to use this card for both new business and reaching out to old business.

Target Market(s)

This should target businesses and referrals to businesses from our existing clients as well as a new client outreach for our new location.

Industry/Entity Type

Computer

Requirements
Must have
• This postcard will let clients know we have moved into or we continue to service their area. Make sure it says Inc, not LLC. Must incorporate existing theme in some fashion.
Nice to have
• Themes to communicate: team of people standing by, stability, faster response time, accessibility.
• Areas of coverage: Westchester, Rockland, Manhattan, The Bronx, lower Connecticut.
Should not have
• Cartoon feel.

```html
<!DOCTYPE html>
<html lang="en">
<head>
<meta charset="utf-8">
<title>Harborline Computer Consulting – Postcard</title>
<link rel="stylesheet" href="https://fonts.googleapis.com/css2?family=Oswald:wght@500;700&family=Roboto:ital,wght@0,400;0,700;1,400&family=Roboto+Condensed:ital,wght@0,700;1,700&display=swap">
<style>
  :root{
    --white:#ffffff;
    --ink:#111418;
    --navy:#0b4a85;
    --blue:#1466ad;
    --sky:#2fb4e9;
    --red:#d3232b;
    --grey:#3a3d42;
    --photo-light:#e9eef3;
    --photo-mid:#c9d3dc;
  }
  html,body{margin:0;padding:0;overflow:hidden;background:var(--white);}
  .postcard{position:relative;width:1200px;height:779px;overflow:hidden;background:var(--white);font-family:"Roboto",Arial,sans-serif;}
  .backdrop{position:absolute;inset:0;}
  .photo-area{position:absolute;left:470px;top:0;width:730px;height:440px;}

  .brand{position:absolute;left:48px;top:34px;display:flex;align-items:center;gap:14px;}
  .brand-dot{width:58px;height:58px;border-radius:50%;background:var(--navy);}
  .brand-name{font-family:"Roboto Condensed",Arial,sans-serif;font-weight:700;font-size:40px;color:var(--navy);letter-spacing:.5px;line-height:1;}
  .brand-sub{position:absolute;left:120px;top:86px;font-family:"Roboto Condensed",Arial,sans-serif;font-weight:700;font-size:15px;letter-spacing:3px;color:var(--navy);}

  .headline{position:absolute;left:44px;top:118px;margin:0;font-family:"Roboto Condensed",Arial,sans-serif;font-style:italic;font-weight:700;font-size:27px;line-height:1.12;text-transform:uppercase;}
  .headline .accent{color:var(--red);display:block;}
  .headline .main{color:var(--blue);display:block;}

  .benefits{position:absolute;left:52px;top:190px;margin:0;padding:0;list-style:none;font-size:18px;color:var(--grey);line-height:1.25;}
  .benefits li{display:flex;align-items:center;gap:10px;}
  .benefits svg{width:14px;height:14px;}

  .intro{position:absolute;left:48px;top:364px;width:440px;margin:0;font-style:italic;font-size:21px;line-height:1.32;color:var(--white);}

  .coverage-tag{position:absolute;left:640px;top:452px;padding:8px 28px;border-radius:24px;background:var(--white);color:var(--ink);font-family:"Oswald",Arial,sans-serif;font-weight:700;font-size:20px;letter-spacing:7px;text-transform:uppercase;}
  .coverage-list{position:absolute;left:640px;top:506px;margin:0;font-family:"Roboto",Arial,sans-serif;font-size:31px;line-height:1.2;color:var(--white);}

  .contact-heading{position:absolute;left:40px;top:628px;margin:0;font-family:"Oswald",Arial,sans-serif;font-weight:700;font-size:44px;line-height:1;color:var(--ink);text-transform:uppercase;}
  .contact-sub{position:absolute;left:42px;top:682px;font-family:"Oswald",Arial,sans-serif;font-weight:500;font-size:20px;letter-spacing:1px;color:var(--ink);text-transform:uppercase;}
  .phone{position:absolute;left:290px;top:634px;display:flex;align-items:center;gap:16px;}
  .phone svg{width:52px;height:52px;}
  .phone-number{font-family:"Oswald",Arial,sans-serif;font-weight:700;font-size:64px;line-height:1;color:var(--ink);}
  .website{position:absolute;left:760px;top:652px;font-family:"Roboto",Arial,sans-serif;font-weight:700;font-style:italic;font-size:40px;color:var(--navy);}
</style>
</head>
<body>
<div class="postcard">
  <svg class="backdrop" width="1200" height="779" viewBox="0 0 1200 779" aria-hidden="true">
    <defs>
      <linearGradient id="band-blue" x1="0" y1="0" x2="1" y2="1">
        <stop offset="0" stop-color="#1a74bd"/>
        <stop offset="1" stop-color="#0b4a85"/>
      </linearGradient>
    </defs>
    <rect width="1200" height="779" fill="var(--white)"/>
  </svg>

  <svg class="photo-area" viewBox="0 0 730 440" role="img" aria-label="Photo of a smiling office team gathered around a laptop">
    <defs>
      <linearGradient id="photo-fade" x1="0" y1="0" x2="1" y2="0">
        <stop offset="0" stop-color="#ffffff"/>
        <stop offset=".35" stop-color="#e9eef3"/>
        <stop offset="1" stop-color="#c9d3dc"/>
      </linearGradient>
    </defs>
    <rect width="730" height="440" fill="url(#photo-fade)"/>
  </svg>

  <svg class="backdrop" width="1200" height="779" viewBox="0 0 1200 779" aria-hidden="true">
    <path d="M0,306 C400,318 850,375 1200,394 V430 C850,412 400,352 0,338 Z" fill="#2fb4e9"/>
    <path d="M0,338 C400,352 850,412 1200,430 V604 H0 Z" fill="url(#band-blue)"/>
    <rect x="0" y="604" width="1200" height="14" fill="#2a2d31"/>
    <rect x="0" y="758" width="1200" height="21" fill="#2a2d31"/>
  </svg>

  <div class="brand">
    <span class="brand-dot"></span>
    <span class="brand-name">HARBORLINE</span>
  </div>
  <span class="brand-sub">COMPUTER CONSULTING, INC</span>

  <h1 class="headline">
    <span class="accent">The highest compliments</span>
    <span class="main">our clients can offer are referrals.</span>
  </h1>

  <ul class="benefits">
    <li><svg viewBox="0 0 14 14"><path d="M1 7 L5 11 L13 2" fill="none" stroke="#1466ad" stroke-width="3"/></svg>Stability</li>
    <li><svg viewBox="0 0 14 14"><path d="M1 7 L5 11 L13 2" fill="none" stroke="#1466ad" stroke-width="3"/></svg>Accessibility</li>
    <li><svg viewBox="0 0 14 14"><path d="M1 7 L5 11 L13 2" fill="none" stroke="#1466ad" stroke-width="3"/></svg>Faster response time</li>
    <li><svg viewBox="0 0 14 14"><path d="M1 7 L5 11 L13 2" fill="none" stroke="#1466ad" stroke-width="3"/></svg>Team of people standing by</li>
  </ul>

  <p class="intro">We are a mobile computer consulting company, taking care of client's issues remotely or at their site.</p>

  <span class="coverage-tag">Areas of coverage</span>
  <p class="coverage-list">Westchester, Rockland, Manhattan,<br>The Bronx, lower Connecticut</p>

  <h2 class="contact-heading">Contact us</h2>
  <span class="contact-sub">For more details</span>

  <div class="phone">
    <svg viewBox="0 0 52 52" aria-hidden="true">
      <rect x="2" y="2" width="48" height="48" rx="10" fill="#111418"/>
      <path d="M12 20 C12 12 40 12 40 20 L40 24 L33 24 L33 20 L19 20 L19 24 L12 24 Z" fill="#fff"/>
      <path d="M16 26 H36 L40 40 H12 Z" fill="#fff"/>
      <circle cx="26" cy="33" r="4" fill="#111418"/>
    </svg>
    <span class="phone-number">98-7654-321</span>
  </div>

  <span class="website">www.qr-lumotek.com</span>
</div>
</body>
</html>
```